M Zyvantics Buisness Cards

I need a technology focused clean business card for my employees. I have attached out logo to include in the mocks. We're a modern tech consulting firm that drives to interface humanity with technology in a truly cohesive fashion.

```html
<!DOCTYPE html>
<html lang="en">
<head>
<meta charset="utf-8">
<title>M Zyvantics Business Cards</title>
<link href="https://fonts.googleapis.com/css2?family=Roboto:wght@400;500;700&family=Fira+Sans:wght@500&display=swap" rel="stylesheet">
<style>
  :root {
    --backdrop: #a8a8a8;
    --brand-blue: #1b6fb8;
    --brand-blue-deep: #1765ab;
    --card-white: #f4f4f4;
    --ink-grey: #77787b;
    --ink-dark: #2e2e2e;
    --accent-blue: #1d6db5;
    --disc-grey: #dcdcdd;
  }
  * { margin: 0; padding: 0; box-sizing: border-box; }
  html, body {
    width: 1200px;
    height: 1138px;
    overflow: hidden;
    background: var(--backdrop);
    font-family: "Roboto", Arial, sans-serif;
  }
  .card {
    position: absolute;
    left: 274px;
    width: 622px;
    height: 374px;
    border-radius: 14px;
    overflow: hidden;
  }
  .card-front {
    top: 186px;
    background: linear-gradient(180deg, var(--brand-blue) 0%, var(--brand-blue-deep) 100%);
    display: flex;
    align-items: center;
    justify-content: center;
  }
  .card-front .decor-disc {
    position: absolute;
    left: -110px;
    top: -10px;
    width: 400px;
    height: 400px;
    border-radius: 50%;
    background: rgba(255, 255, 255, 0.05);
  }
  .wordmark {
    position: relative;
    font-family: "Roboto", Arial, sans-serif;
    font-weight: 700;
    letter-spacing: 1px;
    display: flex;
    align-items: center;
    gap: 14px;
    white-space: nowrap;
  }
  .wordmark-dot {
    border-radius: 50%;
    flex: none;
  }
  .card-front .wordmark {
    color: #ffffff;
    font-size: 52px;
  }
  .card-front .wordmark-dot {
    width: 22px;
    height: 22px;
    background: #ffffff;
  }
  .card-back {
    top: 608px;
    background: var(--card-white);
  }
  .card-back .decor-disc {
    position: absolute;
    left: -22px;
    top: 34px;
    width: 304px;
    height: 304px;
    border-radius: 50%;
    background: var(--disc-grey);
  }
  .card-back .wordmark {
    position: absolute;
    top: 38px;
    right: 36px;
    color: var(--ink-grey);
    font-size: 36px;
    gap: 10px;
  }
  .card-back .wordmark-dot {
    width: 14px;
    height: 14px;
    background: var(--accent-blue);
  }
  .person {
    position: absolute;
    right: 34px;
    top: 154px;
    text-align: right;
  }
  .person-name {
    font-family: "Fira Sans", Arial, sans-serif;
    font-weight: 500;
    font-size: 23px;
    color: var(--accent-blue);
    line-height: 30px;
  }
  .person-title {
    font-size: 15px;
    color: var(--ink-dark);
    line-height: 22px;
  }
  .contact {
    position: absolute;
    right: 34px;
    top: 266px;
    list-style: none;
    text-align: right;
    font-size: 16px;
    color: var(--ink-dark);
  }
  .contact li {
    display: flex;
    justify-content: flex-end;
    align-items: center;
    gap: 7px;
    height: 21px;
  }
  .contact .icon {
    width: 14px;
    height: 14px;
    flex: none;
  }
  .contact .address {
    margin-top: 6px;
  }
</style>
</head>
<body>
  <section class="card card-front">
    <span class="decor-disc" aria-hidden="true"></span>
    <div class="wordmark"><span class="wordmark-dot"></span><span>M Zyvantics</span></div>
  </section>

  <section class="card card-back">
    <span class="decor-disc" aria-hidden="true"></span>
    <div class="wordmark"><span class="wordmark-dot"></span><span>M Zyvantics</span></div>

    <div class="person">
      <p class="person-name">Alden Moreau</p>
      <p class="person-title">Managing Director</p>
    </div>

    <ul class="contact">
      <li>555.014.2290
        <svg class="icon" viewBox="0 0 14 14" aria-hidden="true"><path d="M1 4c0-2 2-3 6-3s6 1 6 3v1h-3V4H4v1H1z M3 6h8l2 6H1z" fill="#1d6db5"/><circle cx="7" cy="9" r="1.6" fill="#f4f4f4"/></svg>
      </li>
      <li>alden@zyvantics.example
        <svg class="icon" viewBox="0 0 14 14" aria-hidden="true"><rect x="1" y="3" width="12" height="9" fill="#1d6db5"/><path d="M1 3l6 5 6-5" fill="none" stroke="#f4f4f4" stroke-width="1.2"/></svg>
      </li>
      <li>www.zyvantics.example
        <svg class="icon" viewBox="0 0 14 14" aria-hidden="true"><circle cx="7" cy="7" r="6" fill="#1d6db5"/><path d="M1 7h12M7 1v12" fill="none" stroke="#f4f4f4" stroke-width="0.8"/><ellipse cx="7" cy="7" rx="2.6" ry="6" fill="none" stroke="#f4f4f4" stroke-width="0.8"/></svg>
      </li>
      <li class="address">48 Harbor Lane, Westfield, US 10472</li>
    </ul>
  </section>
</body>
</html>
```